BSC Flyer to attract applicants 11x17

Brightline Stagecraft Company provides crew for local concerts, filming, theater, and corporate events.
The flyer will be posted on bulletin boards at colleges with theater programs.
Our primary venues are historic theaters in downtown LA
Need a 11x17 poster to attract potential applicants/crew
I have attached a poster that one of our staff made that has all if the relevant info - but i know the poster can look much better than that. I have also attached many images and our logo. It is not necessary to use all of the images, or any of them. The two images of the theater interiors are the venues we operate so they would be the first to include. I can send additional info or images upon request. Thank you

Entertainment

• APPLY@BSCCREWHUB.LA

```html
<!DOCTYPE html>
<html lang="en">
<head>
<meta charset="utf-8">
<title>Brightline Stagecraft Company — Open Positions</title>
<link rel="stylesheet" href="https://fonts.googleapis.com/css2?family=Anton&family=Questrial&family=Didact+Gothic&display=swap">
<style>
  :root {
    --surround: #a8a8a8;
    --ink: #0b090d;
    --white: #ffffff;
    --blue: #2a62c4;
    --photo-warm: #6a3a22;
    --photo-mid: #3a2236;
    --photo-deep: #140f1a;
  }
  * { box-sizing: border-box; margin: 0; padding: 0; }
  html, body {
    width: 832px; height: 1200px; overflow: hidden;
    background: var(--surround);
  }
  .poster {
    position: absolute; left: 71px; top: 67px;
    width: 689px; height: 1065px;
    background: var(--ink);
    overflow: hidden;
    font-family: "Questrial", sans-serif;
    color: var(--white);
  }
  .venue-photo {
    position: absolute; left: 0; top: 70px; width: 689px; height: 770px;
    background:
      radial-gradient(ellipse 60% 45% at 50% 55%, rgba(190,120,70,.55), transparent 70%),
      radial-gradient(ellipse 90% 60% at 50% 50%, var(--photo-warm), var(--photo-mid) 55%, var(--photo-deep) 85%);
    -webkit-mask-image: linear-gradient(to bottom, transparent 0%, #000 18%, #000 85%, transparent 100%);
            mask-image: linear-gradient(to bottom, transparent 0%, #000 18%, #000 85%, transparent 100%);
  }
  .kicker {
    position: absolute; top: 34px; left: 0; width: 100%;
    text-align: center; font-size: 11px; letter-spacing: 8px;
    color: var(--blue);
  }
  .brand {
    position: absolute; top: 130px; left: 0; width: 100%;
    display: flex; flex-direction: column; align-items: center; gap: 18px;
  }
  .brand-dot {
    width: 96px; height: 96px; border-radius: 50%;
    background: var(--white);
  }
  .brand-name {
    font-family: "Anton", sans-serif; font-size: 28px; letter-spacing: 1px;
    color: var(--white); text-align: center; line-height: 1.1;
  }
  .headline {
    position: absolute; top: 368px; left: 0; width: 100%;
    text-align: center;
    font-family: "Anton", sans-serif; font-size: 104px; line-height: 0.86;
    color: var(--white); letter-spacing: 1px;
  }
  .pitch {
    position: absolute; left: 42px; top: 850px; width: 300px;
    font-family: "Didact Gothic", sans-serif; font-size: 19px; line-height: 1.33;
  }
  .pitch .accent { color: var(--blue); }
  .apply {
    position: absolute; right: 42px; top: 864px; text-align: right;
  }
  .apply-rule {
    display: block; margin-left: auto; width: 37px; height: 2px;
    background: var(--white); margin-bottom: 20px;
  }
  .apply-label {
    font-size: 11px; letter-spacing: 3.5px; color: var(--blue); font-weight: bold;
  }
  .apply-email {
    margin-top: 12px; font-size: 18px; letter-spacing: 1.6px;
  }
  .footer-band {
    position: absolute; left: 0; bottom: 0; width: 100%; height: 53px;
    background: var(--white);
    display: flex; align-items: center; justify-content: center;
    font-size: 12px; letter-spacing: 3.5px; color: var(--blue); font-weight: bold;
  }
</style>
</head>
<body>
  <main class="poster">
    <div class="venue-photo" role="img" aria-label="Interior of a historic downtown theater: ornate stage and auditorium with rows of red seats"></div>

    <p class="kicker">BRIGHTLINE STAGECRAFT COMPANY</p>

    <div class="brand">
      <span class="brand-dot"></span>
      <p class="brand-name">BRIGHTLINE STAGECRAFT<br>COMPANY</p>
    </div>

    <h1 class="headline">HAS OPEN<br>POSITIONS</h1>

    <p class="pitch">we are looking for <span class="accent">talented technicians</span> to add to our roster of skilled professionals</p>

    <div class="apply">
      <span class="apply-rule"></span>
      <p class="apply-label">SEND RESUME TO</p>
      <p class="apply-email">APPLY@BSCCREWHUB.LA</p>
    </div>

    <footer class="footer-band">WWW.BSCCREWHUB.LA</footer>
  </main>
</body>
</html>
```